Tolvix Landing Page

We need a web design for an e-commerce website that allows user to sell and buy products from other users.
We would like the website design to:
- show all posted items tiled across the webpage that dynamically resizes depending on the size of the user's screen and appears endless so that users can keep on scrolling down.
- Show a map button where user can choose the area where they want to filter by.
- show search field
- drop down button to choose product category from
- show under each item a requested price and a current highest offer by prospect buyers.

We have attached a sample of a mockup that we have done before but did not quite like the design, however it will give you an idea of what the posted item will look like. The "share" and "heart" logo can be removed and can appear when user hover their mouse across the picture or if user is using mobile when they click on the item.

Ideally we would like the design to be tidy, flawless and very user friendly with blue themed color.

Industry/Entity Type

E-Commerce

```html
<!DOCTYPE html>
<html lang="en">
<head>
<meta charset="utf-8">
<title>Tolvix – Buy and Sell</title>
<link href="https://fonts.googleapis.com/css2?family=Open+Sans:wght@400;600;700&display=swap" rel="stylesheet">
<style>
:root{
  --navy:#2d3b4f;
  --navy-dark:#233042;
  --ink:#1e1e1e;
  --yellow:#f5c000;
  --yellow-dark:#e0a900;
  --white:#ffffff;
  --paper:#f6f6f6;
  --line:#dedede;
  --grey:#6b6b6b;
  --grey-light:#9a9a9a;
  --slate:#5f7088;
  --card-foot:#eeeeee;
}
*{box-sizing:border-box;margin:0;padding:0}
html,body{width:835px;height:1200px;overflow:hidden}
body{position:relative;font-family:"Open Sans",Arial,sans-serif;background:var(--paper);color:var(--grey)}
.abs{position:absolute}

/* header */
.site-header{position:absolute;left:0;top:0;width:835px;height:36px;background:var(--navy)}
.menu-icon{position:absolute;left:167px;top:12px;width:12px;height:10px;border-top:2px solid var(--white);border-bottom:2px solid var(--white)}
.menu-icon::after{content:"";position:absolute;left:0;top:2px;width:12px;height:2px;background:var(--white)}
.brand{position:absolute;left:190px;top:7px;display:flex;align-items:center;gap:4px;color:var(--white);font-weight:700;font-size:17px;line-height:20px}
.brand-dot{width:12px;height:12px;border-radius:50%;background:var(--yellow)}
.main-nav{position:absolute;right:0;top:0;height:36px;display:flex;align-items:center;font-size:8px;font-weight:600;color:var(--white)}
.main-nav span{margin-right:20px}
.btn-login{background:var(--yellow);color:var(--white);width:41px;height:17px;display:flex;align-items:center;justify-content:center;margin-right:179px !important}

/* hero */
.hero{position:absolute;left:0;top:36px;width:835px;height:256px;background:radial-gradient(ellipse at 50% 45%,#6f6f6f 0%,#4a4a4a 45%,#262626 100%)}
.hero-title{position:absolute;left:206px;top:120px;color:var(--white);font-size:24px;font-weight:400;letter-spacing:-.3px}
.search-frame{position:absolute;left:209px;top:152px;width:406px;height:37px;background:rgba(40,52,70,.85);padding:6px}
.search-row{display:flex;height:25px;gap:2px}
.field{background:var(--white);font-size:7px;color:#aaa;display:flex;align-items:center;padding-left:8px;position:relative}
.field.name{width:96px}
.field.cat{width:94px}
.field.area{width:93px}
.field .caret{position:absolute;right:8px;top:11px;border-left:3px solid transparent;border-right:3px solid transparent;border-top:4px solid #999}
.btn-search{flex:1;background:var(--yellow);color:var(--white);font-size:7px;font-weight:700;display:flex;align-items:center;justify-content:center;gap:8px}

/* trending */
.trending{position:absolute;left:0;top:292px;width:835px;height:38px;background:var(--white)}
.trending-label{position:absolute;left:167px;top:11px;font-size:13px;font-weight:700;color:var(--yellow)}
.trend-arrow{position:absolute;top:14px;width:7px;height:7px;border-left:1.5px solid #888;border-bottom:1.5px solid #888}
.trend-arrow.prev{left:270px;transform:rotate(45deg)}
.trend-arrow.next{left:649px;transform:rotate(-135deg)}
.partner-list{position:absolute;left:290px;top:11px;width:355px;display:flex;justify-content:space-between;font-size:11px;font-weight:700;color:#9a9a9a}

/* products */
.section-title{position:absolute;left:0;width:835px;text-align:center;font-weight:700}
.products-title{top:351px;font-size:13.5px;color:var(--grey)}
.products-sub{top:367px;font-size:6.5px;color:var(--grey)}
.card{position:absolute;top:395px;width:118px;height:147px;background:var(--white);border:1px solid var(--line)}
.card-badge{height:14px;font-size:5.5px;color:var(--yellow-dark);font-weight:600;padding:4px 0 0 6px}
.card.active .card-badge{background:var(--yellow);color:var(--white)}
.card-photo{position:absolute;left:8px;top:18px;width:100px;height:70px;background:linear-gradient(135deg,#e9e9e9,#c8c8c8)}
.card-name{position:absolute;left:6px;top:96px;font-size:7.5px;color:#555}
.card.active .card-name{font-weight:700;color:#333}
.card-foot{position:absolute;left:0;bottom:0;width:100%;height:28px;background:var(--card-foot);font-size:5.5px;color:#666}
.card.active .card-foot{background:#9ea3aa;color:var(--white)}
.foot-col{position:absolute;top:4px}
.foot-col.left{left:6px}
.foot-col.right{right:6px;text-align:right}
.foot-col strong{display:block;margin-top:3px;font-size:9px;color:var(--yellow-dark);font-weight:700}
.foot-col.right strong{color:#777}
.card.active .foot-col strong{color:var(--white)}
.plus{display:inline-block;width:6px;height:6px;border-radius:50%;background:var(--yellow);margin-left:3px;vertical-align:middle}
.card-tools{position:absolute;right:0;top:0;display:flex}
.card-tools span{width:14px;height:14px;background:#8a8f96;margin-left:1px;display:flex;align-items:center;justify-content:center}

.missing-title{top:575px;font-size:7.5px;color:var(--grey)}
.missing-sub{top:590px;font-size:6px;color:var(--grey);font-weight:400}
.btn-yellow{position:absolute;background:var(--yellow);color:var(--white);font-weight:700;display:flex;align-items:center;justify-content:center}
.btn-trade{left:365px;top:611px;width:94px;height:20px;font-size:6.5px}

/* compare */
.compare{position:absolute;left:0;top:649px;width:835px;height:173px;background:var(--navy)}
.compare-title{top:21px;font-size:13.5px;color:#dde3ec;font-weight:600}
.compare-sub{top:38px;font-size:6.5px;color:var(--white)}
.offer-list{position:absolute;left:286px;top:62px;display:flex}
.offer{width:71px;height:50px;padding-left:0;color:var(--white);font-size:5.5px;border-right:1px solid #4a5a72;margin-right:10px}
.offer:last-child{border-right:none}
.offer-brand{font-size:9.5px;font-weight:700;margin-bottom:6px;display:flex;align-items:center;gap:3px}
.offer-brand .dot{width:8px;height:8px;border-radius:50%;background:var(--yellow)}
.offer-price{font-size:9.5px;margin-bottom:2px}
.offer-price small{font-size:6px}
.btn-compare{left:377px;top:127px;width:72px;height:20px;font-size:8px}

/* benefits */
.benefits{position:absolute;left:0;top:822px;width:835px;height:138px;background:var(--paper)}
.benefits-title{top:21px;font-size:13.5px;color:var(--slate)}
.benefits-sub{top:39px;font-size:6px;color:#444}
.benefit{position:absolute;top:66px;width:80px;text-align:center;font-size:7.5px;font-weight:700;color:var(--slate)}
.benefit-icon{width:30px;height:30px;border:1.5px solid var(--yellow);border-radius:50%;margin:0 auto 8px;display:flex;align-items:center;justify-content:center}

/* footer */
.site-footer{position:absolute;left:0;top:960px;width:835px;height:210px;background:var(--navy);color:#c9d0da}
.foot-links{position:absolute;top:18px;width:90px}
.foot-links h4{font-size:7.5px;font-weight:400;color:var(--white);padding-bottom:6px;border-bottom:1px solid #4a5a72;margin-bottom:6px}
.foot-links li{list-style:none;font-size:5px;line-height:9.5px}
.payments{position:absolute;left:208px;top:102px;display:flex;align-items:center;font-size:7px;color:var(--white)}
.pay-label{margin-right:14px}
.pay-card{width:23px;height:14px;background:var(--white);margin-right:6px;display:flex;align-items:center;justify-content:center;font-size:4.5px;font-weight:700;color:var(--navy)}
.about-co{position:absolute;left:208px;top:134px;width:215px;font-size:5px;line-height:7px}
.about-co h4{font-size:7.5px;font-weight:400;color:var(--yellow);margin-bottom:5px}
.about-co p{margin-bottom:6px}
.contacts{position:absolute;left:481px;top:134px;width:132px}
.contacts h4{font-size:7.5px;font-weight:400;color:var(--white);margin-bottom:6px}
.contact-line{font-size:5.5px;color:var(--white);font-weight:700;padding:4px 0 6px;border-bottom:1px solid #4a5a72;margin-bottom:2px}
.contact-line em{font-style:normal;color:var(--yellow)}
.contact-line span{font-weight:400}

.bottom-bar{position:absolute;left:0;top:1170px;width:835px;height:30px;background:var(--ink);font-size:5px;color:#aaa}
.copyright{position:absolute;left:208px;top:12px}
.bottom-links{position:absolute;left:476px;top:12px}
</style>
</head>
<body>

<header class="site-header">
  <div class="menu-icon"></div>
  <div class="brand"><span class="brand-dot"></span>Tolvix</div>
  <nav class="main-nav">
    <span>About Us</span>
    <span>Sign up</span>
    <span class="btn-login">Login</span>
  </nav>
</header>

<section class="hero" role="img" aria-label="Dark monochrome photo of assorted second-hand items laid out on a table">
  <h1 class="hero-title" style="top:84px">Find Your Favourate item...</h1>
  <div class="search-frame" style="top:116px">
    <div class="search-row">
      <div class="field name">Type Search Name</div>
      <div class="field cat">Product Category<span class="caret"></span></div>
      <div class="field area">Select Area<span class="caret"></span></div>
      <div class="btn-search">
        <svg width="12" height="9" viewBox="0 0 12 9"><circle cx="3.5" cy="3.5" r="2.5" fill="none" stroke="#fff" stroke-width="1.3"/><line x1="5.5" y1="5.5" x2="9" y2="8" stroke="#fff" stroke-width="1.5"/></svg>
        SEARCH NOW
      </div>
    </div>
  </div>
</section>

<section class="trending">
  <div class="trending-label">Trending Now</div>
  <span class="trend-arrow prev"></span>
  <div class="partner-list">
    <span>Halvern</span><span>Korvel</span><span>Brinto</span><span>Ovane</span><span>Brask</span><span>Zentra</span>
  </div>
  <span class="trend-arrow next"></span>
</section>

<h2 class="section-title products-title">Find Your&nbsp; product list here. Or Choose any one</h2>
<p class="section-title products-sub" style="font-weight:400">We send you a shipping kit, track your shipment, and deposit your proceeds on time.</p>

<article class="card" style="left:167px">
  <div class="card-badge">Ending in 4 hrs</div>
  <div class="card-photo" role="img" aria-label="Photo of a desktop computer with a large display"></div>
  <div class="card-name">Lumo Desk 27</div>
  <div class="card-foot">
    <div class="foot-col left">Latest Offer<strong>$320<span class="plus"></span></strong></div>
    <div class="foot-col right">Asking Price<strong>$799</strong></div>
  </div>
</article>

<article class="card active" style="left:290px">
  <div class="card-badge">Ending in 4 hrs</div>
  <div class="card-tools">
    <span><svg width="8" height="8" viewBox="0 0 8 8"><path d="M1 7V3h2M5 1h2v2M7 1L3.5 4.5" fill="none" stroke="#fff" stroke-width="1"/></svg></span>
    <span><svg width="8" height="8" viewBox="0 0 8 8"><path d="M4 7L1 4a1.6 1.6 0 013-2 1.6 1.6 0 013 2z" fill="none" stroke="#fff" stroke-width="1"/></svg></span>
  </div>
  <div class="card-photo" role="img" aria-label="Photo of several smartphones standing side by side"></div>
  <div class="card-name">Novaphones</div>
  <div class="card-foot">
    <div class="foot-col left">Latest Offer<strong>$120<span class="plus" style="background:#333"></span></strong></div>
    <div class="foot-col right">Asking Price<strong>$699</strong></div>
  </div>
</article>

<article class="card" style="left:414px">
  <div class="card-badge">Ending in 4 hrs</div>
  <div class="card-photo" role="img" aria-label="Photo of two tablets"></div>
  <div class="card-name">Novapad</div>
  <div class="card-foot">
    <div class="foot-col left">Latest Offer<strong>$320<span class="plus"></span></strong></div>
    <div class="foot-col right">Asking Price<strong>$799</strong></div>
  </div>
</article>

<article class="card" style="left:538px">
  <div class="card-badge">Ending in 4 hrs</div>
  <div class="card-photo" role="img" aria-label="Photo of three compact cameras in different colours"></div>
  <div class="card-name">Kestrel Snap</div>
  <div class="card-foot">
    <div class="foot-col left">Latest Offer<strong>$320<span class="plus"></span></strong></div>
    <div class="foot-col right">Asking Price<strong>$799</strong></div>
  </div>
</article>

<h3 class="section-title missing-title">Don't see what you want to sell or buy products above?</h3>
<p class="section-title missing-sub">Trade in DVDs, CDs, cameras, consoles, and more</p>
<div class="btn-yellow btn-trade">TRADE IN OTHER STUF</div>

<section class="compare">
  <h2 class="section-title compare-title">Get the Most Cash for Your Lumo Desk 27</h2>
  <p class="section-title compare-sub">Compare the cash you can make on Tolvix to offers from other online services.</p>
  <div class="offer-list">
    <div class="offer"><div class="offer-brand"><span class="dot"></span>Tolvix</div><div class="offer-price"><small>$</small>200</div>Cash</div>
    <div class="offer"><div class="offer-brand">Marketly</div><div class="offer-price"><small>$</small>298</div>marketly gift card</div>
    <div class="offer"><div class="offer-brand">Zentra</div><div class="offer-price"><small>$</small>200</div>Cash</div>
    <div class="offer"><div class="offer-brand">Arcline</div><div class="offer-price"><small>$</small>200</div>In store Credit</div>
  </div>
  <div class="btn-yellow btn-compare">COMPARE</div>
</section>

<section class="benefits">
  <h2 class="section-title benefits-title">Why use Tolvix?</h2>
  <p class="section-title benefits-sub">Whether you're buying or selling, Tolvix has you covered.</p>
  <div class="benefit" style="left:277px">
    <div class="benefit-icon"><svg width="14" height="14" viewBox="0 0 14 14"><rect x="1" y="1" width="12" height="12" fill="none" stroke="#f5c000" stroke-width="1.3"/><path d="M3 10l3-3 2 2 3-4" fill="none" stroke="#f5c000" stroke-width="1.3"/></svg></div>
    Get top $$
  </div>
  <div class="benefit" style="left:372px">
    <div class="benefit-icon"><svg width="14" height="14" viewBox="0 0 14 14"><path d="M1 5h12l-1.5 7h-9z" fill="none" stroke="#f5c000" stroke-width="1.3"/><path d="M4 5l3-4 3 4M5 7v3M7 7v3M9 7v3" fill="none" stroke="#f5c000" stroke-width="1.1"/></svg></div>
    Save Big
  </div>
  <div class="benefit" style="left:464px">
    <div class="benefit-icon"><svg width="14" height="14" viewBox="0 0 14 14"><rect x="2.5" y="6" width="9" height="7" fill="none" stroke="#f5c000" stroke-width="1.3"/><path d="M4.5 6V4a2.5 2.5 0 015 0v2" fill="none" stroke="#f5c000" stroke-width="1.3"/><circle cx="7" cy="9.5" r="1" fill="#f5c000"/></svg></div>
    Tolvix Guarantee
  </div>
</section>

<footer class="site-footer">
  <div class="foot-links" style="left:208px"><h4>Information</h4><ul><li>About Us</li><li>Delivery</li><li>Privacy Policy</li><li>Terms &amp; Condition</li></ul></div>
  <div class="foot-links" style="left:314px"><h4>Customer Services</h4><ul><li>Contact Us</li><li>Custom Link</li><li>Site Map</li></ul></div>
  <div class="foot-links" style="left:420px"><h4>Extra</h4><ul><li>Brand</li><li>Gift Vouchers</li><li>Affiliates</li><li>Special</li></ul></div>
  <div class="foot-links" style="left:522px"><h4>My Account</h4><ul><li>My Account</li><li>Order History</li><li>Wishlist</li><li>Newsletter</li></ul></div>

  <div class="payments">
    <span class="pay-label">Accept Payments:</span>
    <span class="pay-card">Cardeo</span>
    <span class="pay-card">Payvo</span>
    <span class="pay-card">Vexa</span>
    <span class="pay-card">Marketly</span>
    <span class="pay-card">Orbix</span>
  </div>

  <div class="about-co">
    <h4>About Company Name</h4>
    <p>Industry Lorem Ipsum is simply dummy text of the printing and typesetting industry Lorem Ipsum is simply dummy text of the printing and typesetting industry Lorem Ipsum is simply dummy text of the printing and typesetting industry Lorem Ipsum is simply dummy text of the printing and typesetting.</p>
    <p>Industry Lorem Ipsum is simply dummy text of the printing and typesetting industry Lorem Ipsum is simply dummy text of the printing and typesetting industry.</p>
  </div>

  <div class="contacts">
    <h4>Contacts</h4>
    <div class="contact-line">Location Name : <em>555 0142 88</em> <span>( Toll Free )</span></div>
    <div class="contact-line">Location Name : <em>555 0142 88</em> <span>( Toll Free )</span></div>
  </div>
</footer>

<div class="bottom-bar">
  <span class="copyright">Copyright © 2014 Company Name</span>
  <span class="bottom-links">Home &nbsp;|&nbsp; My Cart &nbsp;|&nbsp; Checkout &nbsp;|&nbsp; Completed Order &nbsp;|&nbsp; Contact Us</span>
</div>

</body>
</html>
```